accomplished personal trainer, former elite gymnast from Russia, highly professional and experienced

Established Fitness trainer in California requires a new web site to attract personal clients and build her group exercise classes.

Here is an example of another fitness trainer's site that I really liked the technology:
http://www.tedmolvin.com

Below I have inserted my current web site: www.quorbalfitnesslodi.com
You can use this web site for the principal content, such as my background and qualifications.

Target Market(s)

Anyone who wants to improve their fitness levels and wellness in general. Anyone who needs directions and instruction on how to exercise. I can train anyone from elite athlete to a disabled person.

Industry/Entity Type

Fitness

Coding

Coded - Design and coding required

Number of Pages Required

5+ page

Font styles to use
Sans Serif

Requirements
Must have
• Easy to navigate main info about me, location, services, contact, benefits of using my services.
• Would be great to create unique representation of me as a trainer and a person, using new technologies and new ideas. Make it different from the other websites. Having its own character. Not too complicated and heavy with information, but an eye catching, useful and fun to navigate.
Nice to have
• new technology, easy access to information, the idea of enjoyment of life, lightness about achieving any goal, spiritual wisdom, unique design. I am planning to insert educational videos, advise, maybe jokes. Sign in, shopping cart, logo, should be easy for me to make changes in content.
Should not have
• cliché, outdated technology, too complicated,

```html
<!DOCTYPE html>
<html lang="en">
<head>
<meta charset="utf-8">
<title>Quorbal Fitness Lodi</title>
<link href="https://fonts.googleapis.com/css2?family=Open+Sans:wght@400;600;700&family=Roboto:wght@400;500;700&display=swap" rel="stylesheet">
<style>
:root{
  --green:#3db40f;
  --ink:#333;
  --muted:#555;
  --dark:#1e2120;
  --red:#e0393e;
}
*{margin:0;padding:0;box-sizing:border-box}
html,body{width:1200px;height:3704px;overflow:hidden;background:#fff}
body{font-family:"Open Sans",Arial,sans-serif;color:var(--ink);position:relative}
h1,h2,h3,.nav a,.logo{font-family:"Roboto",Arial,sans-serif}
.abs{position:absolute}

/* header */
.site-header{position:absolute;top:0;left:0;width:1200px;height:82px;background:#fff}
.logo{position:absolute;left:48px;top:22px;font-size:32px;font-weight:700;letter-spacing:1px;color:#222}
.nav{position:absolute;right:26px;top:32px;display:flex;gap:62px}
.nav a{font-size:15px;color:#222;text-decoration:none;text-transform:uppercase;letter-spacing:.5px}

/* hero */
.hero{position:absolute;top:82px;left:0;width:1200px;height:555px;
  background:
    radial-gradient(ellipse 30% 40% at 20% 45%,rgba(240,235,225,.45),transparent 70%),
    radial-gradient(ellipse 35% 45% at 62% 48%,rgba(60,50,45,.35),transparent 70%),
    linear-gradient(180deg,#3f5a22 0%,#6e8f3a 22%,#a9c46b 42%,#8fbd4a 58%,#6aa92c 78%,#4f8c1f 100%)}
.hero-box{position:absolute;left:385px;top:240px;width:474px;height:118px;background:rgba(40,40,40,.55);text-align:center}
.hero-box h1{font-size:42px;font-weight:400;color:#fff;letter-spacing:1px;margin-top:10px}
.btn-outline{display:inline-block;margin-top:6px;border:2px solid #fff;color:#fff;font-size:14px;padding:7px 28px;font-family:"Roboto",sans-serif}

/* about */
.about-photo{left:45px;top:684px;width:395px;height:328px;
  background:radial-gradient(ellipse 28% 48% at 50% 52%,#8a6650 0%,#4a362b 50%,#0c0b0b 100%)}
.about-text{left:500px;top:675px;width:640px}
.section-title{font-size:32px;font-weight:500;letter-spacing:1px;color:#222;text-transform:uppercase}
.title-rule{width:170px;height:3px;background:var(--green);margin:14px 0 22px}
.about-text p{font-size:14px;line-height:1.6;color:var(--muted);margin-bottom:18px}
.about-text .cert{font-weight:700;font-size:14px;color:#333;margin-bottom:8px}
.about-text ul{list-style:none}
.about-text li{font-size:14px;color:var(--muted);line-height:1.55;padding-left:18px;position:relative}
.about-text li:before{content:"";position:absolute;left:2px;top:7px;border-left:7px solid var(--green);border-top:4px solid transparent;border-bottom:4px solid transparent}

/* why choose */
.why{top:1062px;left:0;width:1200px;height:451px}
.why-photo{position:absolute;left:0;top:0;width:568px;height:451px;
  background:
    radial-gradient(ellipse 18% 26% at 55% 62%,rgba(236,90,150,.75),transparent 70%),
    linear-gradient(180deg,#2f5a1f 0%,#4f7f2c 40%,#83b24a 62%,#9cc35c 100%)}
.why-panel{position:absolute;left:568px;top:0;width:632px;height:451px;background:var(--green);color:#fff;padding:22px 20px 0 20px}
.why-panel h2{font-size:30px;font-weight:500;line-height:1.1;text-transform:uppercase}
.why-panel h2 .big{font-size:38px}
.why-panel h2 .brand{font-size:28px}
.why-intro{font-size:14px;line-height:1.5;margin:8px 0 24px 10px}
.feature{position:relative;padding-left:34px;margin-bottom:22px}
.feature-icon{position:absolute;left:-48px;top:0;width:54px;height:54px}
.feature h3{font-size:14px;font-weight:700;font-family:"Open Sans",sans-serif}
.feature p{font-size:12.5px;line-height:1.55}

/* trainers */
.trainers-title{top:1560px;left:0;width:1200px;text-align:center}
.trainers-title .title-rule{margin:14px auto 0}
.trainer{width:341px;text-align:center}
.trainer-photo{width:341px;height:341px}
.trainer-social{position:relative;width:270px;height:62px;margin:-56px auto 0;background:#fff;display:flex;justify-content:center;align-items:center;gap:30px}
.diamond{width:34px;height:34px;transform:rotate(45deg);background:#ececec;border:1px solid #ddd}
.trainer-role{font-size:12px;color:var(--red);margin-top:18px}
.trainer-name{font-size:14px;color:#555;margin-top:8px;font-family:"Roboto",sans-serif;text-transform:uppercase}

/* healthy mind */
.healthy{top:2136px;left:0;width:1200px;height:432px;
  background:
    radial-gradient(ellipse 40% 60% at 50% 75%,rgba(70,80,60,.5),transparent 70%),
    linear-gradient(180deg,#222624 0%,#2f3530 50%,#1c1f1d 100%);
  color:#fff;text-align:center}
.healthy h2{font-size:30px;font-weight:500;margin-top:44px;letter-spacing:1px}
.healthy .title-rule{margin:12px auto 18px}
.healthy .quote{font-size:17px;margin-bottom:20px}
.healthy .body{width:1000px;margin:0 auto;font-size:14px;line-height:1.7;color:#eee}
.btn-green{display:inline-block;background:var(--green);color:#fff;font-size:14px;padding:14px 22px;margin-top:40px;font-family:"Roboto",sans-serif}

/* testimonials */
.testi-title{top:2615px;left:0;width:1200px;text-align:center}
.testi-title .title-rule{margin:14px auto 0}
.testi-text{left:62px;top:2742px;width:500px}
.testi-text p{font-size:15px;line-height:1.6;color:#444}
.testi-text .author{color:var(--green);margin-top:24px;font-size:14px}
.testi-photo{left:600px;top:2700px;width:540px;height:460px;
  background:
    radial-gradient(ellipse 22% 18% at 68% 30%,rgba(60,150,210,.75),transparent 70%),
    radial-gradient(ellipse 40% 22% at 55% 62%,rgba(210,170,140,.8),transparent 70%),
    radial-gradient(ellipse 20% 16% at 20% 68%,rgba(200,200,205,.9),transparent 70%),
    linear-gradient(180deg,#fff 0%,#fff 80%,#eceaea 90%,#fff 100%)}

/* contact */
.contact{top:3160px;left:0;width:1200px;height:485px;background:linear-gradient(180deg,#2b2f2d,#1f2221);color:#fff}
.contact h2{text-align:center;font-size:34px;font-weight:700;margin-top:42px}
.contact .sub{text-align:center;font-size:15px;margin-top:4px}
.info{position:absolute;left:78px;top:160px;width:500px;font-size:12px}
.info-row{display:flex;margin-bottom:20px}
.info-row dt{width:255px;font-weight:700;text-transform:uppercase}
.info-row dd{line-height:1.55}
.form{position:absolute;left:632px;top:158px;width:508px}
.form-row{display:flex;gap:18px}
.field{height:44px;border:1px solid #555;background:rgba(255,255,255,.04);font-size:12px;color:#bbb;padding:12px 10px;flex:1}
.field.msg{height:128px;margin-top:18px}
.send{margin-top:20px;height:52px;background:var(--green);text-align:center;line-height:52px;font-weight:700;font-size:15px}

/* footer */
.site-footer{position:absolute;top:3645px;left:0;width:1200px;height:59px;background:var(--green);color:#fff;text-align:center;line-height:59px;font-size:14px}
</style>
</head>
<body>

<header class="site-header">
  <div class="logo">QUORBAL FITNESS LODI</div>
  <nav class="nav"><a>Home</a><a>About me</a><a>Location</a><a>Services</a><a>Contact</a></nav>
</header>

<section class="hero" role="img" aria-label="Group of people doing squats together on a park lawn">
  <div class="hero-box">
    <h1>FITNESS OUTDOORS</h1>
    <span class="btn-outline">CONTACT US</span>
  </div>
</section>

<div class="abs about-photo" role="img" aria-label="Portrait of the trainer in sportswear against a dark background"></div>
<section class="abs about-text">
  <h2 class="section-title">Exercise Training</h2>
  <div class="title-rule"></div>
  <p>Mira Volkova is the owner of Quorbal Fitness. She was born and raised in Vologda, Russia where she was a competitive gymnast. Mira graduated from Northern Academy of Sport with a bachelor degree in Kinesiology and Sports Science.</p>
  <p>For more than 20 years, Mira has worked as choreographer, gymnastics coach, and fitness professional.</p>
  <div class="cert">Certified by NFCA as a</div>
  <ul>
    <li>Personal Trainer</li>
    <li>Group Exercise Instructor</li>
    <li>Medical Exercise Specialist</li>
    <li>Orthopedic Exercise Specialist</li>
  </ul>
</section>

<section class="abs why">
  <div class="why-photo" role="img" aria-label="Woman stretching in a split on grass outdoors"></div>
  <div class="why-panel">
    <h2>Why<br><span class="big">Choose</span> <span class="brand">Quorbal</span></h2>
    <p class="why-intro">Mira Volkova is the owner of Quorbal Fitness. She was born and raised in Vologda, Russia where she was a competitive gymnast.</p>
    <div class="feature">
      <svg class="feature-icon" viewBox="0 0 54 54"><circle cx="27" cy="27" r="26" fill="#fff"/><circle cx="27" cy="27" r="22" fill="#3db40f"/><circle cx="27" cy="21" r="6" fill="#fff"/><path d="M16 37c0-7 5-10 11-10s11 3 11 10z" fill="#fff"/></svg>
      <h3>Professional Trainer</h3>
      <p>Mira Volkova is the owner of Quorbal Fitness. She was born and raised<br>in Vologda, Russia where she was a competitive gymnast.</p>
    </div>
    <div class="feature">
      <svg class="feature-icon" viewBox="0 0 54 54"><circle cx="27" cy="27" r="26" fill="#fff"/><circle cx="27" cy="27" r="22" fill="none" stroke="#3db40f" stroke-width="2"/><path d="M27 15l3.5 7.5 8 .8-6 5.4 1.8 8L27 32.6 19.7 36.7l1.8-8-6-5.4 8-.8z" fill="#111"/></svg>
      <h3>Exclusive Accessories</h3>
      <p>Mira Volkova is the owner of Quorbal Fitness. She was born and raised<br>in Vologda, Russia where she was a competitive gymnast.</p>
    </div>
    <div class="feature">
      <svg class="feature-icon" viewBox="0 0 54 54"><circle cx="27" cy="27" r="26" fill="#fff"/><circle cx="27" cy="27" r="22" fill="none" stroke="#3db40f" stroke-width="2"/><text x="27" y="37" text-anchor="middle" font-family="Roboto,sans-serif" font-size="28" font-weight="700" fill="#111">$</text></svg>
      <h3>Money Back Guarantee</h3>
      <p>Mira Volkova is the owner of Quorbal Fitness. She was born and raised<br>in Vologda, Russia where she was a competitive gymnast.</p>
    </div>
  </div>
</section>

<div class="abs trainers-title">
  <h2 class="section-title">World Best Trainers</h2>
  <div class="title-rule"></div>
</div>
<article class="abs trainer" style="left:59px;top:1647px">
  <div class="trainer-photo" role="img" aria-label="Trainer smiling in a gym" style="background:radial-gradient(ellipse 40% 30% at 65% 78%,rgba(120,70,160,.85),transparent 70%),radial-gradient(ellipse 22% 45% at 8% 60%,rgba(240,120,40,.8),transparent 70%),linear-gradient(135deg,#efe6dc,#d9c2ad 55%,#b89a86)"></div>
  <div class="trainer-social"><span class="diamond"></span><span class="diamond"></span><span class="diamond"></span></div>
  <div class="trainer-role">Personal Trainer</div>
  <div class="trainer-name">Tessa Moran</div>
</article>
<article class="abs trainer" style="left:430px;top:1647px">
  <div class="trainer-photo" role="img" aria-label="Trainer with a towel in a gym" style="background:radial-gradient(ellipse 45% 22% at 50% 62%,rgba(250,250,250,.95),transparent 70%),radial-gradient(ellipse 20% 30% at 88% 70%,rgba(90,90,95,.7),transparent 70%),linear-gradient(160deg,#cfc8bf,#a59a8e 60%,#7a7169)"></div>
  <div class="trainer-social"><span class="diamond"></span><span class="diamond"></span><span class="diamond"></span></div>
  <div class="trainer-role">Pilates Trainer</div>
  <div class="trainer-name">Owen Brasky</div>
</article>
<article class="abs trainer" style="left:797px;top:1647px">
  <div class="trainer-photo" role="img" aria-label="Trainer sitting beside an exercise ball" style="background:radial-gradient(circle at 82% 28%,#3a3a3c 0,#3a3a3c 14%,transparent 15%),radial-gradient(ellipse 20% 15% at 18% 78%,rgba(225,60,70,.8),transparent 70%),linear-gradient(135deg,#f4f4f4,#d6d6d6 60%,#b5b5b5)"></div>
  <div class="trainer-social"><span class="diamond"></span><span class="diamond"></span><span class="diamond"></span></div>
  <div class="trainer-role">Weight Trainer</div>
  <div class="trainer-name">Clara Wendt</div>
</article>

<section class="abs healthy" role="img" aria-label="Dim park scene with people exercising in the background">
  <h2>HEALTHY MIND, HEALTHY BODY</h2>
  <div class="title-rule"></div>
  <p class="quote">"Give your life some new energy"</p>
  <p class="body">You have the opportunity today to learn, to grow, to achieve and to experience new things. To do so youthe courage to let go of some old, comfortable, predictable things. A wonderful sereny has taken possessoul, like these sweet mornings of spring. Duis aute rure dolor in reprehdet in voluptate velit esse cillu. A wonderful sereny has taken possession of my entire soul.</p>
  <span class="btn-green">GET MEMBERSHIP NOW</span>
</section>

<div class="abs testi-title">
  <h2 class="section-title">What Our Happy Clients Says</h2>
  <div class="title-rule"></div>
</div>
<section class="abs testi-text">
  <svg width="56" height="46" viewBox="0 0 56 46"><path d="M0 46V24C0 10 6 2 20 0l2 6C14 8 11 13 11 20h11v26zM32 46V24C32 10 38 2 52 0l2 6c-8 2-11 7-11 14h11v26z" fill="#3db40f"/></svg>
  <p style="margin-top:18px">Nullam porttitor lacus a lorem consectetur aliquet. Aenean rutrum augue mauris. Cras elit nibh, malesuada eget sodales non, dignissim eget elit. Quisque lectus mi, posuere non elit nec, imperdiet pulvinar leo. Curabitur semper id massa id pulvinar. Mauris laoreet mollis tortor. Morbi ac nulla in nibh tempor pharetra. Curabitur commodo, enim at fermentum convallis,</p>
  <p class="author">- Lena Hart</p>
</section>
<div class="abs testi-photo" role="img" aria-label="Smiling woman stretching forward on the floor"></div>

<section class="abs contact">
  <h2>GET IN TOUCH</h2>
  <p class="sub">Have a question for us?</p>
  <dl class="info">
    <div class="info-row"><dt>Operating hours:</dt><dd>Monday to Friday 10:00 to 23:00.<br>Saturdays 12:00 to 00:00.<br>Sundays 14:00 to 22:00.<br><br>Closed on public holidays.</dd></div>
    <div class="info-row"><dt>Address:</dt><dd>214 Orchard Lane, Lodi,<br>CA 95240</dd></div>
    <div class="info-row"><dt>Telephone:</dt><dd>+1 55 010 2468</dd></div>
    <div class="info-row"><dt>Fax:</dt><dd>+1 55 010 2468</dd></div>
    <div class="info-row"><dt>Email:</dt><dd>info@example.com</dd></div>
  </dl>
  <div class="form">
    <div class="form-row"><div class="field">Name *</div><div class="field">Email *</div><div class="field">Subject *</div></div>
    <div class="field msg">Message *</div>
    <div class="send">Send Message</div>
  </div>
</section>

<footer class="site-footer">© copyright 2016, All Rights Reserved &nbsp;Privacy Policy &nbsp;| Terms and Conditions</footer>

</body>
</html>
```